zipbeatz.net website for a mobile DJ entertainment company

I am looking for a business card design for a mobile DJ company. We perform all types of events from weddings to kids parties and I would like a card to be fun, bright, energetic and give the impression of a great time. I am also attempting to creating a visual brand and recognition by leveraging a custom vinyl wrap that I am using for my vehicle and trailer using paint splatter. I would like the design on the front to look like multi-color paint splatter across the card with the company website "ZIPBEATZ.net" prominently displayed and my contact information on the back. The back can be more plain then the front with just contact information with maybe a muted version of the front as a background.

Contact Information for Business Card

See above

Font styles to use
Serif

Colors
9bcb3b
0293ce
ec1f27
fbed22
6b449b
f78f20

Requirements
Nice to have
• Would like ti close enough to my truck to be recognized as one product.

```html
<!DOCTYPE html>
<html lang="en">
<head>
<meta charset="utf-8">
<title>ZIPBEATZ.net business card</title>
<link href="https://fonts.googleapis.com/css2?family=Michroma&family=Open+Sans:wght@400&display=swap" rel="stylesheet">
<style>
  :root {
    --stage: #2a2a2b;
    --paper: #fbfbfa;
    --ink: #141414;
    --green: #9bcb3b;
    --blue: #0293ce;
    --red: #ec1f27;
    --yellow: #fbed22;
    --purple: #6b449b;
    --orange: #f78f20;
  }
  * { margin: 0; padding: 0; box-sizing: border-box; }
  html, body { width: 1200px; height: 900px; overflow: hidden; }
  body { background: var(--stage); position: relative; font-family: "Open Sans", sans-serif; }

  .card {
    position: absolute;
    width: 560px;
    height: 320px;
    background: var(--paper);
    border-radius: 28px;
    overflow: hidden;
    box-shadow: 0 14px 30px rgba(0,0,0,.45);
  }
  .card--front { left: 70px; top: 90px; }
  .card--back { left: 570px; top: 480px; }

  .splatter { position: absolute; inset: 0; }
  .splatter--front {
    background: linear-gradient(100deg,
      var(--purple) 0%, var(--green) 18%, var(--blue) 38%,
      var(--orange) 56%, var(--yellow) 74%, var(--red) 90%);
    clip-path: polygon(0 22%, 30% 8%, 62% 0, 100% 0, 100% 58%, 72% 78%, 40% 95%, 8% 100%, 0 100%);
    opacity: .92;
  }
  .splatter--back {
    background: linear-gradient(115deg,
      var(--purple) 0%, var(--green) 22%, var(--blue) 42%,
      var(--orange) 62%, var(--red) 82%, var(--yellow) 100%);
    clip-path: polygon(0 30%, 22% 22%, 40% 40%, 62% 70%, 82% 88%, 70% 100%, 0 100%);
    opacity: .9;
  }

  .wordmark {
    position: absolute;
    left: 0; right: 0; top: 128px;
    text-align: center;
    font-family: "Michroma", sans-serif;
    font-size: 52px;
    letter-spacing: 3px;
    color: var(--ink);
    white-space: nowrap;
  }
  .wordmark__tld { font-size: 18px; letter-spacing: 2px; }

  .contact {
    position: absolute;
    right: 46px; top: 66px;
    width: 240px;
    color: var(--ink);
  }
  .contact__name {
    font-family: "Michroma", sans-serif;
    font-size: 17px;
    font-variant: small-caps;
    letter-spacing: 2px;
    margin-bottom: 10px;
  }
  .contact__row {
    display: flex; align-items: center; gap: 8px;
    font-size: 14px; line-height: 22px;
    padding-left: 26px;
  }
  .contact__row svg { width: 14px; height: 14px; flex: none; }
</style>
</head>
<body>

<section class="card card--front">
  <div class="splatter splatter--front" role="img" aria-label="Multicolour paint splatter in purple, green, blue, orange, yellow and red sweeping across the card"></div>
  <div class="wordmark">ZIPBEATZ<span class="wordmark__tld">.net</span></div>
</section>

<section class="card card--back">
  <div class="splatter splatter--back" role="img" aria-label="Multicolour paint splatter rising from the lower left corner"></div>
  <div class="contact">
    <p class="contact__name">Your Name</p>
    <p class="contact__row">
      <svg viewBox="0 0 16 16"><path d="M2 5c0-2 2-3 6-3s6 1 6 3v1h-3V5H5v1H2z M4 7h8l2 6H2z" fill="#141414"/><circle cx="8" cy="10" r="1.6" fill="#fff"/></svg>
      000 000 0000
    </p>
    <p class="contact__row">
      <svg viewBox="0 0 16 16"><rect x="1" y="3" width="14" height="10" fill="#141414"/><path d="M1 3l7 6 7-6" fill="none" stroke="#fff" stroke-width="1.2"/></svg>
      youremail@xyz.com
    </p>
    <p class="contact__row">
      <svg viewBox="0 0 16 16" fill="none" stroke="#141414" stroke-width="1.1"><circle cx="8" cy="8" r="6.5"/><ellipse cx="8" cy="8" rx="3" ry="6.5"/><path d="M1.5 8h13M3 4.5h10M3 11.5h10"/></svg>
      yourwebsite.com
    </p>
  </div>
</section>

</body>
</html>
```